Gordon Pellbrook Consulting - Web Design Project

We need a web design for my new edgy consulting business specializing in innovation, technology and strategy.

It is our personal goal to turn each client into raving fans by helping them achieve their own business goals and aspirations through assisting them in raising their own innovation and marketing standards.

We provide our personalised and state-of-the-art services to our clients and boards who represent some of the world greatest innovative thinkers.
Updates

Here is some other information which may help shape your thinking.

I've had direct Involvement in the development of the following iPad, iPhone Applications and websites

FarbeyondOzlands.com (TerraLink platform) by Voyage Bureau
http://farbeyondozlands.example.au

Sail Verve by Bright Voyaging
https://apps.example-store.com/au/app/sail-verve/id100000001

uRedlandTR by Travel Territory Board
https://apps.example-store.com/au/app/uredlandtr/id100000002

Wexmoor Trips
http://www.wexmoortrips.example.au

Trek Mapper by Voyage Bureau
http://apps.example-store.com/au/app/trek-mapper/id100000003

Sunward by Sunward Travel Office
https://apps.example-store.com/au/app/sunward/id100000004

Upper Fernridge Valley Route by Visit Coastlands
https://apps.example-store.com/au/app/upper-fernridge-valley-route/id100000005

Wanderer Path by Travel Territory Board and Southern Plains Travel Council
https://apps.example-store.com/au/app/wanderers-path-grand-journey/id100000006

Gordon Pellbrook Consulting (GPC)
November 2012 – Present (8 months)Brisbane, Sydney, Canberra

Gordon’s consults to Small-to-Medium Enterprises (SME) and Government organisations on business strategy, technology strategy, risk mitigation, disruptive technology and innovation in the workplace.

Gordon’s consultancy mantra is that we cannot divorce economic life from cultural life particularly in an era when social capital may be as important as physical capital in business.

Reason: request from designers, I want to see their best efforts

Target Market(s)

35+

Industry/Entity Type

Business

Requirements
Must have
• Please use some of the personal image(s) contained in the zip files which can be downloaded from here

http://filedrop.example/k9Xq2Lm
http://filedrop.example/p4Rt7Vn
http://filedrop.example/z8Hw3Bc
Nice to have
• Black, Sleek design, maybe minimalist. Nice to have a Pixelle for the design. Nice to have it easily ported to Wordpress or be a modified Wordpress template. HTML 5, responsive design

```html
<!DOCTYPE html>
<html lang="en">
<head>
<meta charset="utf-8">
<title>Gordon Pellbrook Consulting</title>
<link href="https://fonts.googleapis.com/css2?family=Tinos:wght@400;700&family=Lato:wght@400;700&display=swap" rel="stylesheet">
<style>
:root{
  --backdrop:#ececec;
  --page:#ffffff;
  --band:#efefef;
  --ink:#222226;
  --muted:#55575c;
  --tab:#c9ced6;
  --dark:#2c2b2e;
  --footer:#29282d;
  --blue:#7aa6d8;
  --green:#b7dca0;
}
*{margin:0;padding:0;box-sizing:border-box}
html,body{width:1200px;height:1000px;overflow:hidden}
body{background:var(--backdrop);font-family:'Tinos',serif;color:var(--ink)}
.page{position:absolute;left:457px;top:0;width:285px;height:1000px;background:var(--page);box-shadow:0 0 14px rgba(0,0,0,.08);overflow:hidden}
.abs{position:absolute}
.nav-tab{left:18px;top:0;width:25px;height:45px;background:var(--tab)}
.nav-item{top:14px;width:34px;text-align:center;font-family:'Lato',sans-serif;font-size:4.6px;line-height:1.3;color:var(--ink)}
.nav-item svg{display:block;margin:0 auto 3px}
.nav-tab .nav-item{left:-4px;color:#fff}
.brand{right:20px;top:6px;text-align:center;font-family:'Lato',sans-serif}
.brand-name{font-size:13px;letter-spacing:1px;color:#555}
.brand-sub{font-size:3.6px;color:#777;line-height:1.2}
.hero-img{left:0;top:63px;width:285px;height:107px;background:linear-gradient(90deg,#eef0ef 0%,#dfe4e0 40%,#c9d1cd 100%)}
.hero-person{left:160px;top:38px;width:125px;height:132px;background:linear-gradient(180deg,#c8b6a5 0%,#8e98a5 45%,#6f7c8c 100%)}
.hero-title{left:28px;top:78px;font-size:16.5px;line-height:1.15;color:#3d3d3f}
.hero-title .line2{font-size:17.5px;color:#222}
.hero-sub{left:28px;top:119px;font-size:5.4px;color:#7b7e80}
.hero-sign{left:85px;top:139px;font-size:8px;color:#444}
.pillars{left:25px;top:205px;width:115px;height:85px}
.pillar-label{font-size:4.6px;font-weight:700;text-align:center;width:50px}
.about{left:155px;top:191px;width:110px}
.about h2{font-weight:400;font-size:9.4px;line-height:1.2;margin-bottom:6px}
.about p{font-size:4.6px;line-height:1.45;color:var(--muted);margin-bottom:6px}
.band{left:0;width:285px;background:var(--band)}
.band-text{font-size:9.5px;line-height:1.25;color:#222}
.band-body{font-size:4.6px;line-height:1.4;color:var(--muted)}
.btn{background:var(--dark);color:#fff;font-family:'Lato',sans-serif;font-weight:700;font-size:5px;text-align:center;line-height:11px;height:11px}
.h-sect{font-size:9.5px;line-height:1.25}
.desc{font-size:4.6px;line-height:1.4;color:var(--muted)}
.thumb{border-radius:50%;width:27px;height:27px}
.app-icon{width:24px;height:24px;border-radius:4px}
.app-text{font-size:4.6px;line-height:1.35;color:#333}
.footer{left:0;top:968px;width:285px;height:32px;background:var(--footer)}
.footer-text{left:0;width:200px;top:13px;text-align:right;font-family:'Lato',sans-serif;font-size:3.8px;color:#9a9a9e}
.social{top:12px;width:7px;height:7px;background:#6e6e73}
</style>
</head>
<body>
<div class="page">
  <div class="abs nav-tab">
    <div class="abs nav-item" style="top:14px">
      <svg width="8" height="8" viewBox="0 0 8 8"><path d="M4 0 0 4h1v4h2V5h2v3h2V4h1z" fill="#333"/></svg>Home
    </div>
  </div>
  <div class="abs nav-item" style="left:48px">
    <svg width="8" height="8" viewBox="0 0 8 8"><circle cx="3" cy="2.2" r="1.8" fill="none" stroke="#222" stroke-width="1"/><rect x="0.8" y="4.6" width="5.2" height="3" rx=".6" fill="none" stroke="#222" stroke-width="1"/></svg>About<br>Us
  </div>
  <div class="abs nav-item" style="left:83px">
    <svg width="8" height="8" viewBox="0 0 8 8"><circle cx="3.3" cy="3.3" r="2.6" fill="none" stroke="#222" stroke-width="1"/><path d="M5.2 5.2 7.6 7.6M3.3 2v2.6M2 3.3h2.6" stroke="#222" stroke-width="1"/></svg>Why<br>Choose Us?
  </div>
  <div class="abs nav-item" style="left:118px">
    <svg width="8" height="8" viewBox="0 0 8 8"><rect x=".5" y="1.5" width="7" height="5" rx=".6" fill="#222"/><path d="M.8 2 4 4.5 7.2 2" stroke="#fff" stroke-width=".7" fill="none"/></svg>Contact<br>Us
  </div>
  <div class="abs brand">
    <div class="brand-name">GPC</div>
    <div class="brand-sub">gordon pellbrook<br>consultant</div>
  </div>

  <div class="abs hero-img" role="img" aria-label="Bright office interior with window light, softly blurred"></div>
  <div class="abs hero-person" role="img" aria-label="Portrait of Gordon Pellbrook in a light grey suit"></div>
  <div class="abs hero-title">We are new edgy<br><span class="line2">Consulting Business</span></div>
  <div class="abs hero-sub">specializing in innovation, technology and strategy</div>
  <div class="abs hero-sign">– Gordon Pellbrook</div>

  <svg class="abs pillars" viewBox="0 0 115 85">
    <ellipse cx="57" cy="13" rx="10" ry="7" fill="#3d5a8a"/>
    <ellipse cx="57" cy="13" rx="16" ry="3" fill="none" stroke="#3d5a8a" stroke-width="1.6"/>
    <path d="M57 40v9M52.5 44.5h9" stroke="#222" stroke-width="1.2"/>
    <rect x="16" y="45" width="20" height="17" rx="1.5" fill="#fff" stroke="var(--blue)" stroke-width="2"/>
    <rect x="16" y="45" width="20" height="4" fill="var(--blue)"/>
    <path d="M82 45h8M84 45v7l-6 10h16l-6-10v-7" fill="var(--green)" stroke="var(--green)" stroke-width="1.6" stroke-linejoin="round"/>
  </svg>
  <div class="abs pillar-label" style="left:57px;top:232px">STRATEGY</div>
  <div class="abs pillar-label" style="left:24px;top:277px">TECHNOLOGY</div>
  <div class="abs pillar-label" style="left:84px;top:277px">INNOVATION</div>
  <div class="abs about">
    <h2>Gordon Pellbrook<br>Consulting (GPC)</h2>
    <p>November 2012 – Present (8 months) Brisbane,<br>Sydney, Canberra</p>
    <p>Gordon’s consults to Small-to-Medium Enterprises (SME) and Government organisations on business strategy, technology strategy, risk mitigation, disruptive technology and innovation in the workplace.</p>
    <p>Gordon’s consultancy mantra is that we cannot divorce economic life from cultural life particularly in an era when social capital may be as important as physical capital in business.</p>
  </div>

  <div class="abs band" style="top:324px;height:116px"></div>
  <div class="abs" style="left:150px;top:315px;width:105px;height:117px;background:linear-gradient(180deg,#f2f2f2,#d9d9db)" role="img" aria-label="Gordon Pellbrook standing in a dark suit before a sketched business diagram"></div>
  <div class="abs band-text" style="left:32px;top:345px">We provide our<br>personalised and<br>state-of-the-art services</div>
  <div class="abs band-body" style="left:32px;top:384px;width:110px">to our clients and boards who represent some of the world greatest innovative thinkers.</div>
  <div class="abs btn" style="left:105px;top:404px;width:34px">more</div>

  <div class="abs" style="left:10px;top:470px;width:147px;height:90px;background:linear-gradient(180deg,#1b2b4f,#0e1730 80%,#bfc1c4 80%,#d8d9db)" role="img" aria-label="Laptop showing a travel website with a map"></div>
  <div class="abs h-sect" style="left:168px;top:487px">Web<br>Development</div>
  <div class="abs desc" style="left:168px;top:515px;width:95px">direct Involvement in the development of the web project</div>
  <div class="abs thumb" style="left:31px;top:578px;background:linear-gradient(180deg,#2a3a66,#0f1a35)" role="img" aria-label="Website thumbnail"></div>
  <div class="abs desc" style="left:65px;top:588px">farbeyondozlands</div>
  <div class="abs btn" style="left:99px;top:601px;width:34px">GO</div>
  <div class="abs thumb" style="left:159px;top:578px;background:linear-gradient(180deg,#d88a5a,#6d3a2a)" role="img" aria-label="Website thumbnail"></div>
  <div class="abs desc" style="left:193px;top:588px">wexmoortrips.com</div>
  <div class="abs btn" style="left:227px;top:601px;width:34px">GO</div>

  <div class="abs band" style="top:644px;height:111px"></div>
  <div class="abs" style="left:155px;top:628px;width:102px;height:127px;background:linear-gradient(180deg,#c8b4a2 0%,#3a3b40 40%,#1d1e22 100%)" role="img" aria-label="Gordon Pellbrook in a dark suit, waist-up, with soft grey decoration behind"></div>
  <div class="abs band-text" style="left:28px;top:668px">It is our<br>personal goal</div>
  <div class="abs band-body" style="left:28px;top:694px;width:118px;text-align:justify">to turn each client into raving fans by helping them achieve their own business goals and aspirations through assisting them in raising their own innovation and marketing standards.</div>
  <div class="abs btn" style="left:103px;top:727px;width:34px">more</div>

  <div class="abs" style="left:28px;top:764px;width:82px;height:114px;background:linear-gradient(180deg,#1d1d20,#2b2b30 50%,#c98f72 100%);border-radius:10px" role="img" aria-label="Hand holding a smartphone showing a travel app"></div>
  <div class="abs h-sect" style="left:148px;top:790px">Mobile<br>Application<br>Development</div>
  <div class="abs desc" style="left:148px;top:829px;width:95px">direct Involvement in the development of the mobile application.</div>
  <div class="abs" style="left:204px;top:847px;width:33px;height:11px;background:#111;border-radius:1.5px"></div>

  <div class="abs app-icon" style="left:34px;top:892px;background:linear-gradient(#c98a5a,#6e4a35)" role="img" aria-label="App icon"></div>
  <div class="abs app-text" style="left:69px;top:897px">Upper Fernridge Valley Route<br>By Visit Coastlands</div>
  <div class="abs app-icon" style="left:152px;top:890px;background:linear-gradient(#49b6e8,#f0c030)" role="img" aria-label="App icon"></div>
  <div class="abs app-text" style="left:190px;top:897px">Sunward<br>By Sunward Travel Office</div>
  <div class="abs app-icon" style="left:34px;top:930px;background:linear-gradient(#2a7fd0,#1552a0)" role="img" aria-label="App icon"></div>
  <div class="abs app-text" style="left:69px;top:937px">Sail Verve<br>By Bright Voyaging</div>
  <div class="abs app-icon" style="left:152px;top:930px;background:linear-gradient(#8cb0d0,#b06a40)" role="img" aria-label="App icon"></div>
  <div class="abs app-text" style="left:190px;top:937px">The Wanderer's Path -<br>The Grand Journey Drive Holiday<br>By Travel Territory Board</div>

  <div class="abs footer">
    <div class="abs footer-text">Copyright | All Right Reserved 2013 | Terms &amp; Conditions</div>
    <div class="abs social" style="left:216px"></div>
    <div class="abs social" style="left:230px"></div>
    <div class="abs social" style="left:244px"></div>
    <div class="abs social" style="left:258px"></div>
  </div>
</div>
</body>
</html>
```